Veltorquin.io - Please redesign to make it look better from current design

We already have the current website, that you can access but we think it can improve from current version.
Veltorquin is a cryptocurrency hedge fund that allow you to participate in the hedge fund with cryptocurrency such as eth.
At current phase, we are doing an ICO, then we want to make sure that the website it looks professional, beautiful and trustable enough for investors after looking at our website.
Target Market(s)
Investors
Industry/Entity Type
Investment
Coding
Coded - Design and coding required
Number of Pages Required
1 page
Look and feel

```html
<!DOCTYPE html>
<html lang="en">
<head>
<meta charset="utf-8">
<title>Veltorquin.io – Digital Asset Management</title>
<link rel="stylesheet" href="https://fonts.googleapis.com/css2?family=Roboto:wght@300;400;500;700&family=Roboto+Slab:wght@400;700&display=swap">
<style>
:root{
  --blue:#1f8fd6;
  --blue-bright:#2a9ad8;
  --blue-nav:#0e5aa6;
  --navy:#1a2d7a;
  --title-blue:#1d84d0;
  --band:#1a58a6;
  --tile-1:#c9d9ea;
  --tile-2:#7fa7d4;
  --tile-3:#3c74b8;
  --tile-4:#0f4f9e;
  --text:#555;
  --muted:#888;
  --light-bg:#eaf0f6;
  --dark:#222222;
  --map:#9c9c9c;
  --teal:#2a8a7c;
  --deep:#1d3d6c;
}
*{box-sizing:border-box;margin:0;padding:0}
html,body{width:1200px;height:3232px;overflow:hidden}
body{font-family:"Roboto",Arial,sans-serif;color:var(--text);background:#fff;position:relative}
.abs{position:absolute}
.slab{font-family:"Roboto Slab",Georgia,serif}

/* header */
.topbar{left:0;top:0;width:1200px;height:86px;background:var(--blue)}
.brand-zone{left:0;top:0;width:400px;height:86px;background:#fff;clip-path:polygon(0 0,400px 0,350px 86px,0 86px)}
.brand-zone::after{content:"";position:absolute;left:340px;top:0;width:20px;height:86px}
.brand{left:160px;top:24px;font:700 30px "Roboto",Arial,sans-serif;color:var(--navy);display:flex;align-items:center;gap:10px}
.brand i{display:block;width:16px;height:16px;border-radius:50%;background:var(--navy)}
.contact-chip{top:24px;display:flex;gap:12px;align-items:flex-start;color:#fff}
.contact-chip b{display:block;font:700 17px "Roboto",sans-serif}
.contact-chip span{font-size:14px}
.search{left:862px;top:29px;width:176px;height:30px;border:1px solid #fff;border-radius:15px;color:#e4f1fb;font-size:12px;padding:7px 14px}
.search svg{position:absolute;right:6px;top:5px}
.nav{left:0;top:86px;width:1200px;height:48px;background:var(--blue-nav)}
.nav a{position:absolute;top:15px;color:#fff;text-decoration:none;font-size:15px}

/* hero */
.hero{left:0;top:134px;width:1200px;height:476px;background:linear-gradient(180deg,#9fb1c2 0%,#5f7688 45%,#3e4f5c 100%)}
.hero-mark{left:0;width:1200px;top:275px;text-align:center;color:#fff;font:700 22px "Roboto",sans-serif;letter-spacing:2px}
.hero-line1{left:0;width:1200px;top:336px;text-align:center;color:#fff;font:300 27px "Roboto",sans-serif}
.hero-line2{left:0;width:1200px;top:366px;text-align:center;color:#fff;font:700 50px "Roboto Slab",serif}
.hero-arrow{top:351px;width:50px;height:38px;border:1px solid rgba(255,255,255,.6);background:rgba(255,255,255,.12)}
.hero-arrow svg{position:absolute;left:13px;top:12px}
.dots{left:566px;top:551px;display:flex;gap:6px}
.dots i{width:9px;height:9px;border-radius:50%;background:rgba(255,255,255,.55)}
.dots i:first-child{background:#fff}

/* offer */
.intro-title{left:162px;top:674px;font:700 36px "Roboto Slab",serif;color:var(--title-blue)}
.intro-sub{left:162px;top:716px;font-size:17px;color:var(--title-blue);letter-spacing:.5px}
.intro-copy{left:162px;top:748px;width:230px;font-size:11px;line-height:17px;color:var(--muted)}
.btn-outline{left:162px;top:842px;width:135px;height:37px;border:2px solid var(--blue);border-radius:19px;color:var(--blue);text-align:center;font-size:15px;line-height:33px}
.offer-box{left:403px;top:635px;width:635px;height:280px;background:var(--blue-bright);clip-path:polygon(38px 0,100% 0,100% 100%,0 100%,0 34px)}
.offer-title{left:403px;width:635px;top:650px;text-align:center;font:400 32px "Roboto Slab",serif;color:#fff}
.offer-col{top:720px;width:200px;text-align:center;color:#fff}
.offer-col .ico{width:50px;height:50px;border:2px solid #fff;border-radius:50%;margin:0 auto 10px}
.offer-col h3{font:400 16px "Roboto",sans-serif;line-height:19px}
.offer-col h3 b{display:block;font-weight:700}
.offer-col p{font-size:11px;line-height:16px;margin-top:6px;color:#eaf5fc}
.offer-col .pill{display:inline-block;margin-top:12px;padding:5px 12px;background:var(--navy);border:1px solid #fff;border-radius:12px;font-size:10px;font-weight:700}
.rule{left:0;width:1200px;height:4px;background:var(--blue)}

/* process */
.process{left:0;top:941px;width:1200px;height:384px;background:var(--light-bg)}
.process h2{left:681px;top:973px;font:700 36px "Roboto Slab",serif;color:var(--title-blue)}
.process .sub{left:681px;top:1016px;font-size:15px;color:var(--title-blue)}
.process .copy{left:681px;top:1048px;width:360px;font-size:10.5px;line-height:17px;color:var(--text)}
.process h3{left:681px;top:1137px;font:500 16px "Roboto",sans-serif;color:var(--title-blue)}
.process ul{left:681px;top:1162px;list-style:none;font-size:10.5px;line-height:19px;color:var(--text);width:380px}
.chart{left:110px;top:1070px}

/* ahead */
.ahead-title{left:162px;top:1362px;font:700 36px "Roboto Slab",serif;color:var(--title-blue)}
.ahead-sub{left:162px;top:1405px;font-size:15px;color:var(--title-blue);letter-spacing:1px}
.service{left:162px;display:flex;gap:14px;width:440px}
.service .ico{flex:none;width:53px;height:53px;border:2px solid var(--title-blue);border-radius:50%;position:relative}
.service .ico::after{content:"";position:absolute;left:14px;top:14px;width:21px;height:21px;border-radius:4px;background:var(--title-blue)}
.service h4{font:500 15px "Roboto",sans-serif;color:var(--title-blue);letter-spacing:.5px;margin-top:3px}
.service p{font-size:11px;line-height:14px;color:var(--text);margin-top:3px}
.meeting{left:629px;top:1329px;width:571px;height:481px;background:linear-gradient(135deg,#e9e6e2 0%,#bdb5ab 50%,#5a4f48 100%)}

/* tiles */
.tile{top:1814px;width:300px;height:271px;text-align:center;color:#fff;padding:48px 28px 0}
.tile .ico{width:34px;height:34px;margin:0 auto 30px}
.tile h4{font:400 18px "Roboto",sans-serif;letter-spacing:.5px}
.tile p{font-size:11px;line-height:15px;margin-top:10px}
.tile.t1{left:0;background:var(--tile-1);color:#24364f}
.tile.t2{left:300px;background:var(--tile-2)}
.tile.t3{left:600px;background:var(--tile-3)}
.tile.t4{left:900px;background:var(--tile-4)}

/* team */
.team-bg{left:0;top:2085px;width:1200px;height:595px;background:#f6f7f9}
.team-title{left:0;width:1200px;top:2126px;text-align:center;font:700 36px "Roboto Slab",serif;color:var(--title-blue)}
.team-sub{left:0;width:1200px;top:2171px;text-align:center;font-size:22px;letter-spacing:3px;color:var(--title-blue)}
.member{top:2227px;width:270px;height:401px;background:#fff;border:1px solid #dde3ea}
.member .photo{height:304px;border:2px solid var(--band)}
.member .name{height:54px;background:var(--band);color:#fff;text-align:center;padding-top:10px}
.member .name b{display:block;font-size:13px;letter-spacing:.3px}
.member .name span{font-size:11px}
.member .social{display:flex;justify-content:center;gap:16px;padding-top:15px}
.member .social i{width:11px;height:11px;border-radius:50%;background:#b8c0c8}

/* contact strip */
.strip{left:0;top:2676px;width:1200px;height:98px;border-top:4px solid var(--blue);background:#fff}
.strip-item{top:2702px;display:flex;gap:14px}
.strip-item small{display:block;font-size:12px;color:var(--title-blue);letter-spacing:.5px}
.strip-item span{font-size:14px;color:#444;line-height:17px}

/* contact form */
.form-zone{left:0;top:2774px;width:629px;height:414px;background:var(--dark)}
.form-zone h2{position:absolute;left:157px;top:36px;font:300 34px "Roboto",sans-serif;color:#eee;letter-spacing:2px}
.field{position:absolute;left:157px;width:422px;height:36px;background:#2c2c2c;border:1px solid #444;border-radius:3px;color:#999;font-size:11px;padding:10px 12px}
.field.msg{height:95px}
.submit{position:absolute;left:159px;top:349px;width:93px;height:35px;background:var(--blue);border-radius:3px;color:#fff;font-size:15px;line-height:35px;text-align:center}
.map{left:629px;top:2774px;width:571px;height:414px;background:var(--map)}
.footer{left:0;top:3188px;width:1200px;height:44px;background:var(--blue);color:#fff}
.footer .copy{position:absolute;left:162px;top:15px;font-size:11px}
.footer .connect{position:absolute;left:840px;top:14px;font-size:13px;display:flex;align-items:center;gap:12px}
.footer .connect i{width:18px;height:18px;border-radius:50%;background:#fff}
</style>
</head>
<body>

<!-- header -->
<div class="abs topbar"></div>
<div class="abs brand-zone"></div>
<div class="abs brand"><i></i>Veltorquin</div>
<div class="abs contact-chip" style="left:489px">
  <svg width="22" height="22" viewBox="0 0 24 24"><path d="M6 2l4 4-2 3c1 2 3 4 5 5l3-2 4 4-3 3C10 19 5 14 3 5z" fill="none" stroke="#fff" stroke-width="1.6"/></svg>
  <div><b>Call Now!</b><span>+88 (010) 555 01 20</span></div>
</div>
<div class="abs contact-chip" style="left:689px">
  <svg width="24" height="22" viewBox="0 0 24 22"><rect x="2" y="4" width="20" height="14" fill="none" stroke="#fff" stroke-width="1.6"/><path d="M2 4l10 8 10-8" fill="none" stroke="#fff" stroke-width="1.6"/></svg>
  <div><b>Email:</b><span>info@veltorquin.io</span></div>
</div>
<div class="abs search">Search Now...
  <svg width="18" height="18" viewBox="0 0 18 18"><circle cx="9" cy="9" r="9" fill="#fff"/><circle cx="8" cy="8" r="3.5" fill="none" stroke="#1f8fd6" stroke-width="1.5"/><path d="M10.5 10.5l3 3" stroke="#1f8fd6" stroke-width="1.5"/></svg>
</div>
<nav class="abs nav">
  <a style="left:160px">Home</a><a style="left:287px">Features</a><a style="left:433px">About Us</a><a style="left:577px">Services</a><a style="left:717px">Blog</a><a style="left:834px">Projects</a><a style="left:969px">Contact Us</a>
</nav>

<!-- hero -->
<div class="abs hero" role="img" aria-label="Businessman standing before a large glass screen showing a world map and financial charts"></div>
<div class="abs hero-mark">VELTORQUIN</div>
<div class="abs hero-line1">WE PROVIDEBEST FINANCIAL SOLUTIONS</div>
<div class="abs hero-line2">FOR YOUR BUSINESS</div>
<div class="abs hero-arrow" style="left:17px"><svg width="24" height="14" viewBox="0 0 24 14"><path d="M23 7H2M8 1L2 7l6 6" fill="none" stroke="#fff" stroke-width="2"/></svg></div>
<div class="abs hero-arrow" style="left:1127px"><svg width="24" height="14" viewBox="0 0 24 14"><path d="M1 7h21M16 1l6 6-6 6" fill="none" stroke="#fff" stroke-width="2"/></svg></div>
<div class="abs dots"><i></i><i></i><i></i></div>

<!-- offer -->
<div class="abs intro-title">VELTORQUIN</div>
<div class="abs intro-sub">Digital Asset Management</div>
<p class="abs intro-copy">Lorem Ipsum is simply dummy text of the printing and typesetting industry. Lorem Ipsum has been the industry's standard dummy text ever since the 1500s.</p>
<div class="abs btn-outline">Details</div>
<div class="abs offer-box"></div>
<div class="abs offer-title">What We Offer!</div>
<div class="abs offer-col" style="left:413px"><div class="ico"></div><h3>MARKET<b>FORECASTING</b></h3><p>Lorem Ipsum is simply dummy text of the printing...</p><span class="pill">➞ READ MORE!</span></div>
<div class="abs offer-col" style="left:622px"><div class="ico"></div><h3>FINANCIAL<b>MODELING</b></h3><p>Lorem Ipsum is simply dummy text of the printing...</p><span class="pill">➞ READ MORE!</span></div>
<div class="abs offer-col" style="left:830px"><div class="ico"></div><h3>FINANCIAL<b>ANALYSIS</b></h3><p>Lorem Ipsum is simply dummy text of the printing...</p><span class="pill">➞ READ MORE!</span></div>
<div class="abs rule" style="top:937px"></div>

<!-- process -->
<section class="abs process"></section>
<h2 class="abs" style="left:681px;top:973px;font:700 36px 'Roboto Slab',serif;color:var(--title-blue)">PROCESS</h2>
<div class="abs" style="left:681px;top:1016px;font-size:15px;color:var(--title-blue)">Hedge Fund Model</div>
<p class="abs" style="left:681px;top:1048px;width:360px;font-size:10.5px;line-height:17px">Veltorquin run on closed-end fund（CEF）model which offers its shares to investors and utilize the fund to speculate and invest in the innovative blockchain tokens. Veltorquin will charge an upfront annual operation fee 4% of the money raised during the ICO. After that, the fund will charge a quarterly performance of 50% on the net profit made.</p>
<h3 class="abs" style="left:681px;top:1137px;font:500 16px 'Roboto',sans-serif;color:var(--title-blue)">Net Profit Distribution</h3>
<ul class="abs" style="left:681px;top:1162px;list-style:none;font-size:10.5px;line-height:19px;width:380px">
  <li>50 % of net profit is distributed to investors</li>
  <li>0 – 5 % net profit &gt; 0% performance fee</li>
  <li>5 – 10% net profit &gt; 5% performance fee</li>
  <li>10–15 % net profit &gt; 13% performance fee</li>
  <li>+ 15% net profit &gt; 15% performance fee</li>
  <li>The remainder（50% minus performance fee, so at least 35%）is reinvested</li>
</ul>
<svg class="abs chart" width="500" height="220" viewBox="0 0 500 220">
  <g stroke="#d5dde6" stroke-width="1">
    <line x1="40" y1="20" x2="480" y2="20"/><line x1="40" y1="65" x2="480" y2="65"/><line x1="40" y1="110" x2="480" y2="110"/><line x1="40" y1="155" x2="480" y2="155"/>
  </g>
  <line x1="40" y1="200" x2="480" y2="200" stroke="#9aa6b2"/>
  <g font-size="9" fill="#777" font-family="Roboto,sans-serif" text-anchor="end">
    <text x="32" y="203">0</text><text x="32" y="158">20</text><text x="32" y="113">40</text><text x="32" y="68">60</text><text x="32" y="23">80</text>
  </g>
  <g font-size="9" fill="#777" font-family="Roboto,sans-serif" text-anchor="middle">
    <text x="40" y="214">0</text><text x="113" y="214">2</text><text x="187" y="214">4</text><text x="260" y="214">6</text><text x="333" y="214">8</text><text x="407" y="214">10</text>
  </g>
  <path d="M70 200 C100 200 110 99 132 99 C154 99 164 200 194 200Z" fill="var(--teal)" opacity=".9"/>
  <path d="M225 200 C250 200 245 110 260 110 C275 110 280 200 300 200Z" fill="var(--teal)" opacity=".9"/>
  <path d="M400 200 C420 200 425 132 442 132 C459 132 464 200 484 200Z" fill="var(--teal)" opacity=".9"/>
  <path d="M130 200 C165 200 165 31 187 31 C209 31 209 200 244 200Z" fill="var(--deep)" opacity=".85"/>
  <path d="M280 200 C310 200 312 65 333 65 C354 65 356 200 386 200Z" fill="var(--deep)" opacity=".85"/>
  <path d="M340 200 C360 200 358 150 372 150 C386 150 392 200 420 200Z" fill="var(--teal)" opacity=".9"/>
</svg>
<div class="abs rule" style="top:1325px;height:4px"></div>

<!-- ahead -->
<h2 class="abs ahead-title">WE ARE ALWAYS AHEAD</h2>
<div class="abs ahead-sub">PROFFESIONAL SOLUTIONS FOR YOUR BUSINESS.</div>
<div class="abs service" style="top:1458px"><div class="ico"></div><div><h4>FINANCIAL PLANNING:</h4><p>Lorem Ipsum is simply dummy text of the printing and typesetting industry. Lorem Ipsum has been the industry's standard...</p></div></div>
<div class="abs service" style="top:1538px"><div class="ico"></div><div><h4>CASH INVESTMENT:</h4><p>Lorem Ipsum is simply dummy text of the printing and typesetting industry. Lorem Ipsum has been the industry's standard...</p></div></div>
<div class="abs service" style="top:1618px"><div class="ico"></div><div><h4>FINANCIAL CONSULTANCY:</h4><p>Lorem Ipsum is simply dummy text of the printing and typesetting industry. Lorem Ipsum has been the industry's standard...</p></div></div>
<div class="abs service" style="top:1698px"><div class="ico"></div><div><h4>RETIREMENT PLANNING:</h4><p>Lorem Ipsum is simply dummy text of the printing and typesetting industry. Lorem Ipsum has been the industry's standard...</p></div></div>
<div class="abs meeting" role="img" aria-label="Business team meeting around a table in a bright office"></div>

<!-- tiles -->
<div class="abs tile t1"><svg class="ico" viewBox="0 0 34 34"><rect x="5" y="4" width="24" height="26" fill="none" stroke="#2a7fc9" stroke-width="2"/><path d="M10 12h14M10 18h14M10 24h8" stroke="#2a7fc9" stroke-width="2"/></svg><h4>INVESTMENT</h4><p>Lorem Ipsum is simply dummy text of the printing and typesetting industry. Lorem Ipsum has been the industry's standard dummy text ever since the 1500s.</p></div>
<div class="abs tile t2"><svg class="ico" viewBox="0 0 34 34"><path d="M2 16l8-6 7 5 7-5 8 6-8 7-7-4-7 4z" fill="none" stroke="#fff" stroke-width="2"/></svg><h4>SALES &amp; TRADING</h4><p>Lorem Ipsum is simply dummy text of the printing and typesetting industry. Lorem Ipsum has been the industry's standard dummy text ever since the 1500s.</p></div>
<div class="abs tile t3"><svg class="ico" viewBox="0 0 34 34"><circle cx="17" cy="17" r="13" fill="none" stroke="#fff" stroke-width="2"/><path d="M17 9v16M21 12h-6a3 3 0 000 5h4a3 3 0 010 5h-6" fill="none" stroke="#fff" stroke-width="2"/></svg><h4>INVESTMENT MANAGEMENT</h4><p>Lorem Ipsum is simply dummy text of the printing and typesetting industry. Lorem Ipsum has been the industry's standard dummy text ever since the 1500s.</p></div>
<div class="abs tile t4"><svg class="ico" viewBox="0 0 34 34"><path d="M4 4v26h26" fill="none" stroke="#fff" stroke-width="2"/><path d="M8 24l7-8 5 5 9-11" fill="none" stroke="#fff" stroke-width="2"/></svg><h4>MARKET RESEARCH</h4><p>Lorem Ipsum is simply dummy text of the printing and typesetting industry. Lorem Ipsum has been the industry's standard dummy text ever since the 1500s.</p></div>

<!-- team -->
<div class="abs team-bg"></div>
<div class="abs team-title">VELTORQUIN</div>
<div class="abs team-sub">EXECUTIVE TEAM</div>
<div class="abs member" style="left:162px"><div class="photo" role="img" aria-label="Portrait of the director" style="background:linear-gradient(180deg,#6b5a4a,#3a3430)"></div><div class="name"><b>DAREN MATTISELO</b><span>DIRECTOR</span></div><div class="social"><i></i><i></i><i></i><i></i></div></div>
<div class="abs member" style="left:465px"><div class="photo" role="img" aria-label="Portrait of the technical advisor" style="background:linear-gradient(180deg,#d8dcc8,#9a9a86)"></div><div class="name"><b>KOVI RANTHALER</b><span>TECHNICAL ADVISOR</span></div><div class="social"><i></i><i></i><i></i><i></i></div></div>
<div class="abs member" style="left:769px"><div class="photo" role="img" aria-label="Portrait of the marketing consultant" style="background:linear-gradient(180deg,#8a2a26,#5a1c1a)"></div><div class="name"><b>JORIN HALBECKWELL</b><span>MARKETING CONSULTANT</span></div><div class="social"><i></i><i></i><i></i><i></i></div></div>

<!-- contact strip -->
<div class="abs strip"></div>
<div class="abs strip-item" style="left:162px">
  <svg width="50" height="46" viewBox="0 0 50 46"><rect x="4" y="14" width="42" height="28" rx="5" fill="none" stroke="#1d84d0" stroke-width="2.5"/><path d="M10 14c0-10 30-10 30 0" fill="none" stroke="#1d84d0" stroke-width="2.5"/><circle cx="25" cy="28" r="7" fill="none" stroke="#1d84d0" stroke-width="2.5"/></svg>
  <div><small>CALL TO NOW!</small><span>+88 (010) 555 01 20</span></div>
</div>
<div class="abs strip-item" style="left:480px">
  <svg width="58" height="46" viewBox="0 0 58 46"><rect x="2" y="6" width="54" height="36" fill="none" stroke="#1a2d7a" stroke-width="2"/><path d="M2 6l27 20 27-20" fill="none" stroke="#1a2d7a" stroke-width="2"/></svg>
  <div><small>EMAIL</small><span>info@veltorquin.io</span></div>
</div>
<div class="abs strip-item" style="left:775px">
  <svg width="32" height="48" viewBox="0 0 32 48"><path d="M16 46C6 30 3 24 3 16a13 13 0 0126 0c0 8-3 14-13 30z" fill="none" stroke="#1d84d0" stroke-width="2.5"/><circle cx="16" cy="16" r="5" fill="none" stroke="#1d84d0" stroke-width="2.5"/></svg>
  <div style="width:240px"><small>VISIT US</small><span style="font-size:11px;line-height:13px">Suites 4-9, 12/F., North Wing, Meridale Trade Centre, 28 Lanterra Road, Westbay District, Port Calden</span></div>
</div>

<!-- contact form -->
<section class="abs form-zone">
  <h2>CONTACT</h2>
  <div class="field" style="top:89px">&#128100; Name:</div>
  <div class="field" style="top:138px">&#9993; Email:</div>
  <div class="field" style="top:188px">&#9743; Phone Number:</div>
  <div class="field msg" style="top:235px">Message:</div>
  <div class="submit">➦ Submit</div>
</section>
<div class="abs map" role="img" aria-label="Street map showing the office location with a marker"></div>

<footer class="abs footer">
  <div class="copy">Copyright ©2017. All rights reserved.</div>
  <div class="connect">Connect with us: <i></i><i></i><i></i></div>
</footer>
</body>
</html>
```